Dance School poster for end of year dance concert for mainly young girls.

We need an A3 portrait poster for our end of year concert.
Designs are attached of posters from previous 2 years as a reference only.
The theme of our concert this year is "Let's Dance" which we want to convey a general feel of energy & fun with dance.
Dance styles in the concert include Jazz & Hip Hop.
Bright colors are preferred in the design.

Target Market(s)

The concert is attended by several hundred family & friends

Industry/Entity Type

Dance Studio

Requirements
Must have
• Must have
• Let's Dance
• BRK logo (file supplied)
• 'The Maribel Crowe Dancers' (font is Mistral)
• Date of the concert: Saturday 14th November 2015
• Pellow Theatre, Saint Fenwick College Dalebrook
Nice to have
• We like clean design with no cluttered imagery.

```html
<!DOCTYPE html>
<html lang="en">
<head>
<meta charset="utf-8">
<title>Let's Dance – The Maribel Crowe Dancers</title>
<link rel="stylesheet" href="https://fonts.googleapis.com/css2?family=Kaushan+Script&family=Yesteryear&family=Ubuntu:wght@400;700&family=Oswald:wght@300;400&display=swap">
<style>
  :root {
    --bg-pink: #f7c6db;
    --bg-pink-deep: #f1b3cf;
    --ink-dark: #2a1a24;
    --venue-purple: #7a2b6c;
    --date-plum: #4a1d48;
    --lets-red: #e3335f;
    --ribbon-white: #ffffff;
    --ribbon-shade: #e8a9c4;
    --dot-white: rgba(255,255,255,0.9);
    --heart-soft: rgba(255,255,255,0.55);
  }
  * { margin: 0; padding: 0; box-sizing: border-box; }
  html, body { width: 853px; height: 1200px; overflow: hidden; }
  body { background: var(--bg-pink); }
  .poster {
    position: relative;
    width: 853px;
    height: 1200px;
    overflow: hidden;
    background: radial-gradient(ellipse at 50% 30%, var(--bg-pink) 0%, var(--bg-pink-deep) 100%);
    font-family: "Ubuntu", sans-serif;
    text-align: center;
  }
  .brand-mark {
    position: absolute;
    top: 38px; left: 0; width: 100%;
    display: flex; justify-content: center; align-items: center; gap: 10px;
  }
  .brand-mark__dot {
    width: 14px; height: 14px; border-radius: 50%;
    background: var(--ink-dark);
  }
  .brand-mark__name {
    font-family: "Kaushan Script", cursive;
    font-size: 44px;
    color: var(--ink-dark);
    line-height: 1;
  }
  .heart-deco {
    position: absolute;
    top: 62px;
    width: 90px; height: 72px;
    border-radius: 40%;
    background: var(--heart-soft);
  }
  .heart-deco--left { left: 112px; }
  .heart-deco--right { right: 92px; }
  .school-name {
    position: absolute;
    top: 100px; left: 0; width: 100%;
    font-family: "Kaushan Script", cursive;
    font-size: 48px;
    color: var(--ink-dark);
  }
  .ribbon {
    position: absolute;
    top: 162px; left: 230px;
    width: 393px; height: 62px;
  }
  .ribbon__label {
    position: absolute;
    inset: 0;
    display: flex; align-items: center; justify-content: center;
    font-family: "Ubuntu", sans-serif;
    font-size: 32px;
    letter-spacing: 2px;
    color: var(--ink-dark);
  }
  .dotted-rule {
    position: absolute;
    top: 248px; left: 85px; width: 683px;
    border-top: 5px dotted var(--dot-white);
  }
  .venue {
    position: absolute;
    top: 284px; left: 0; width: 100%;
    font-size: 32px;
    line-height: 40px;
    color: var(--venue-purple);
  }
  .event-date {
    position: absolute;
    top: 370px; left: 0; width: 100%;
    font-size: 38px;
    font-weight: 700;
    color: var(--date-plum);
  }
  .title-lets {
    position: absolute;
    top: 478px; left: 0; width: 100%;
    font-family: "Oswald", sans-serif;
    font-weight: 400;
    font-size: 72px;
    letter-spacing: 3px;
    color: var(--lets-red);
    line-height: 1;
  }
  .title-dance {
    position: absolute;
    top: 540px; left: 0; width: 100%;
    font-family: "Yesteryear", cursive;
    font-size: 210px;
    line-height: 1;
    color: var(--ink-dark);
  }
  .shard-field {
    position: absolute;
    left: 0; top: 600px;
    width: 853px; height: 600px;
  }
</style>
</head>
<body>
<main class="poster">
  <div class="heart-deco heart-deco--left" role="img" aria-label="Sketched white heart"></div>
  <div class="heart-deco heart-deco--right" role="img" aria-label="Sketched white heart"></div>

  <div class="brand-mark">
    <span class="brand-mark__dot"></span>
    <span class="brand-mark__name">BRK</span>
  </div>

  <h2 class="school-name">The Maribel Crowe Dancers</h2>

  <div class="ribbon">
    <svg width="393" height="62" viewBox="0 0 393 62" aria-hidden="true">
      <polygon points="0,14 40,14 40,58 0,58 14,36" fill="var(--ribbon-shade)"/>
      <polygon points="393,14 353,14 353,58 393,58 379,36" fill="var(--ribbon-shade)"/>
      <rect x="30" y="4" width="333" height="48" fill="var(--ribbon-white)"/>
    </svg>
    <span class="ribbon__label">PRESENTS</span>
  </div>

  <div class="dotted-rule"></div>

  <p class="venue">Pellow Theatre,<br>Saint Fenwick College Dalebrook</p>
  <p class="event-date">Saturday 14th November 2015</p>

  <h1>
    <span class="title-lets">LET'S</span>
    <span class="title-dance">Dance</span>
  </h1>

  <svg class="shard-field" viewBox="0 0 853 600" role="img" aria-label="Burst of colourful geometric triangle shards in purple, magenta, pink and turquoise">
    <defs>
      <linearGradient id="shardTone" x1="0" y1="1" x2="1" y2="0">
        <stop offset="0" stop-color="#7a2f8f"/>
        <stop offset="0.35" stop-color="#c93a8f"/>
        <stop offset="0.65" stop-color="#3fb4d6"/>
        <stop offset="1" stop-color="#f08fba"/>
      </linearGradient>
    </defs>
    <polygon points="0,330 150,290 300,230 450,170 600,120 740,60 853,30 853,600 0,600" fill="url(#shardTone)"/>
  </svg>
</main>
</body>
</html>
```